Book Cover that will be used for a series of books with the NAME changed on each.

Create a book cover from the crude picture I will upload. A solid black background with a streetlamp shining light down on a Man with a trench coat on carrying a briefcase and a revolver. This book is about a hitman, angels, etc. The first book is entitled: Two Pale Birds - The Prelude to The Marigold Ledger series. Author K.R. BLOMVEY on cover please. Thanks.

```html
<!DOCTYPE html>
<html lang="en">
<head>
<meta charset="utf-8">
<title>Two Pale Birds — The Prelude</title>
<link rel="stylesheet" href="https://fonts.googleapis.com/css2?family=Creepster&family=Tinos:wght@400;700&display=swap">
<style>
  :root {
    --ink: #000000;
    --blood: #c3141c;
    --blood-mid: #8e0c12;
    --blood-deep: #3a0507;
    --paper: #ffffff;
  }
  html, body {
    margin: 0;
    padding: 0;
    width: 802px;
    height: 1200px;
    overflow: hidden;
    background: var(--ink);
  }
  .cover {
    position: relative;
    width: 802px;
    height: 1200px;
    background: var(--ink);
    overflow: hidden;
  }
  .author {
    position: absolute;
    left: 34px;
    top: 22px;
    margin: 0;
    font-family: "Tinos", serif;
    font-weight: 400;
    font-size: 38px;
    line-height: 44px;
    letter-spacing: 0.5px;
    color: var(--paper);
  }
  .scene {
    position: absolute;
    left: 40px;
    top: 60px;
    width: 740px;
    height: 680px;
  }
  .title {
    position: absolute;
    left: 0;
    width: 802px;
    top: 728px;
    margin: 0;
    text-align: center;
    font-family: "Creepster", cursive;
    font-weight: 400;
    font-size: 164px;
    line-height: 146px;
    letter-spacing: 2px;
    color: var(--blood);
    text-transform: uppercase;
  }
  .title span { display: block; }
  .series {
    position: absolute;
    left: 0;
    width: 802px;
    top: 1050px;
    text-align: center;
    color: var(--paper);
  }
  .series-lead {
    margin: 0;
    font-family: "Tinos", serif;
    font-weight: 700;
    font-size: 46px;
    line-height: 52px;
  }
  .series-name {
    margin: 4px 0 0;
    font-family: "Tinos", serif;
    font-weight: 400;
    font-size: 30px;
    line-height: 36px;
  }
</style>
</head>
<body>
  <main class="cover">
    <p class="author">K.R. BLOMVEY</p>

    <svg class="scene" viewBox="0 0 740 680" role="img"
         aria-label="Illustration: red blood splatter across the dark behind the silhouette of a man in a trench coat holding a raised revolver beside a glowing streetlamp">
      <defs>
        <radialGradient id="splatter-halo" cx="52%" cy="46%" r="52%">
          <stop offset="0%" stop-color="var(--blood-deep)"/>
          <stop offset="30%" stop-color="var(--blood-mid)" stop-opacity="0.9"/>
          <stop offset="55%" stop-color="var(--blood)" stop-opacity="0.7"/>
          <stop offset="78%" stop-color="var(--blood-mid)" stop-opacity="0.35"/>
          <stop offset="100%" stop-color="var(--ink)" stop-opacity="0"/>
        </radialGradient>
        <radialGradient id="figure-shade" cx="50%" cy="50%" r="50%">
          <stop offset="0%" stop-color="#0a0101"/>
          <stop offset="60%" stop-color="#140203" stop-opacity="0.85"/>
          <stop offset="100%" stop-color="#140203" stop-opacity="0"/>
        </radialGradient>
      </defs>
      <rect width="740" height="680" fill="url(#splatter-halo)"/>
      <ellipse cx="420" cy="360" rx="150" ry="300" fill="url(#figure-shade)"/>
    </svg>

    <h1 class="title"><span>Two</span><span>Pale Birds</span></h1>

    <div class="series">
      <p class="series-lead">THE PRELUDE</p>
      <p class="series-name">to The Marigold Ledger series</p>
    </div>
  </main>
</body>
</html>
```